Islamic App which helps to calculate, track and pay Zakat

We need an application which helps muslim people to calculate and pay Zakat - mandatory donations which muslim should pay based on his income. The application will consist of two parts (applications) - the one which is used by "payer" and another one - used by "receiver". To make a payment "payer" will scan QR-code which "receiver" will generate in his app and show to payer. "Receiver" will have option to initiate cash withdrawal once he collected required minimum for the withdrawal.
Important that "payer" side journey to make a payment should be as short as possible - imaging same as you make donation by cash - you just gave money and left, similar experience should be with app - couple-three taps to make it. For receiver side major requirement is to keep the UI/UX as simple as possible, these guys usually are not aware about online payments (roughly speaking this part of the app should be more similar to Pixora rather than to banking/financial app)
In this Figma I tried to sketch the UX for both sides (just to explain the idea): https://www.plandrafo.com/file/kq4Rt8VbnWxZp2LcMs7Ea9/Draft-basics?type=design&node-id=2741-508316&mode=design

Target Market(s)

Muslims

Industry/Entity Type

Donations

Colors
0094D4
00A9DD
6FCCEA
C7EBF8
E9F6FB
00AB8E
00BBA5
67D7C9
C6EFE9
E9F9F6

Requirements
Must have
• The application should have soul. Design should show that this application intend to help people, not just money transfer
Nice to have
• Payment should be as quick as possible, in the sketches I showed it as banknotes/coins which user need to slide-up to pay. Maybe make it similar as Zelt OS dock icons?
Should not have
• The application should not look as banking/financial app or wallet app

```html
<!DOCTYPE html>
<html lang="en">
<head>
<meta charset="utf-8">
<title>Zakat – Donation and Payment Screens</title>
<link href="https://fonts.googleapis.com/css2?family=Work+Sans:wght@400;500;600&display=swap" rel="stylesheet">
<style>
  :root {
    --page-bg: #e9edf5;
    --navy: #1f3466;
    --navy-deep: #0f1f4d;
    --ink: #3b3b3b;
    --ink-soft: #6e6e6e;
    --muted: #a8acb4;
    --line: #e3e6ec;
    --tray: #e9eef7;
    --white: #ffffff;
    --photo-sky: #8a8f95;
    --photo-city: #8f6a4e;
    --photo-mosque: #c8a071;
  }
  * { box-sizing: border-box; margin: 0; padding: 0; }
  html, body { width: 1200px; height: 1029px; overflow: hidden; }
  body {
    background: var(--page-bg);
    font-family: "Work Sans", sans-serif;
    position: relative;
    color: var(--ink);
  }
  .screen {
    position: absolute;
    border-radius: 34px;
    overflow: hidden;
    background: var(--white);
    box-shadow: 0 20px 50px rgba(40, 55, 90, 0.18);
  }
  .screen--donee { left: 160px; top: 132px; width: 371px; height: 804px; }
  .screen--payment { left: 682px; top: 134px; width: 369px; height: 801px; }

  /* Donee screen */
  .donee-photo {
    position: absolute; left: 0; top: 0; width: 371px; height: 530px;
    background: linear-gradient(180deg, var(--photo-sky) 0%, #a3a19b 28%, var(--photo-city) 42%, var(--photo-mosque) 70%, #9b6e52 100%);
  }
  .icon-btn {
    position: absolute; width: 34px; height: 34px; border-radius: 50%;
    background: var(--white); display: flex; align-items: center; justify-content: center;
    box-shadow: 0 2px 6px rgba(0,0,0,0.2);
  }
  .icon-btn--edit { left: 23px; top: 59px; }
  .icon-btn--menu { left: 315px; top: 56px; width: 30px; height: 30px; }
  .side-tab { position: absolute; left: 322px; top: 265px; }
  .donee-card {
    position: absolute; left: 0; top: 516px; width: 371px; height: 288px;
    background: var(--white); border-radius: 24px 24px 0 0;
  }
  .donee-name { position: absolute; left: 21px; top: 24px; font-size: 28px; font-weight: 600; color: var(--ink); }
  .pay-badge {
    position: absolute; left: 294px; top: 24px; width: 56px; height: 33px;
    background: linear-gradient(180deg, #1f3b7a, var(--navy-deep)); border-radius: 4px;
    color: var(--white); font-size: 9.5px; font-weight: 500; display: flex; align-items: center; justify-content: center; text-align: center; line-height: 1.05;
  }
  .donee-bio { position: absolute; left: 22px; top: 70px; width: 330px; font-size: 14.5px; color: var(--ink-soft); line-height: 29px; letter-spacing: 0.2px; }
  .donee-bio p + p { line-height: 25px; margin-top: 2px; }
  .money-tray {
    position: absolute; left: 21px; top: 164px; width: 329px; height: 91px;
    background: var(--tray); border-radius: 8px;
  }
  .coin {
    position: absolute; left: 24px; top: 21px; width: 48px; height: 48px; border-radius: 50%;
    background: radial-gradient(circle, #ededed, #c9c9c9); border: 2px solid #a9a9a9;
  }
  .banknote { position: absolute; top: 22px; width: 104px; height: 47px; }
  .banknote--red { left: 83px; background: linear-gradient(90deg, #e69a92, #c97d7a 50%, #e6a59d); }
  .banknote--green { left: 205px; background: linear-gradient(90deg, #cfe2bb, #9fc79a 50%, #d6e4bd); }
  .slide-pill {
    position: absolute; left: 114px; top: 244px; width: 143px; height: 24px;
    background: var(--white); border-radius: 12px; box-shadow: 0 2px 6px rgba(40,55,90,0.12);
    display: flex; align-items: center; gap: 8px; padding-left: 3px;
    font-size: 10px; letter-spacing: 0.7px; color: var(--ink-soft);
  }
  .slide-pill__knob { width: 18px; height: 18px; border-radius: 50%; background: var(--navy-deep); display: flex; align-items: center; justify-content: center; }

  /* Payment screen */
  .pay-header {
    position: absolute; left: 0; top: 0; width: 369px; height: 290px;
    background: var(--navy);
  }
  .pay-skyline {
    position: absolute; left: 170px; top: 0; width: 199px; height: 280px;
    background: linear-gradient(90deg, rgba(31,52,102,0) 0%, #2a4683 70%, #2e4b8a 100%);
  }
  .brand-mark { position: absolute; left: 144px; top: 68px; width: 80px; height: 80px; border-radius: 50%; background: var(--white); }
  .brand-name { position: absolute; left: 0; top: 146px; width: 369px; text-align: center; font-size: 34px; font-weight: 500; color: var(--white); }
  .pay-sheet { position: absolute; left: 0; top: 220px; }
  .sheet-toggle {
    position: absolute; left: 166px; top: 243px; width: 38px; height: 38px; border-radius: 50%;
    background: linear-gradient(180deg, #27427f, var(--navy-deep));
    box-shadow: 0 4px 10px rgba(15,31,77,0.35);
    display: flex; align-items: center; justify-content: center;
  }
  .pay-title { position: absolute; left: 0; top: 313px; width: 369px; text-align: center; font-size: 27px; font-weight: 600; color: var(--ink); letter-spacing: 0.3px; }
  .carousel-arrow { position: absolute; top: 381px; width: 25px; height: 25px; border-radius: 50%; border: 1.3px solid #9ba0a8; display: flex; align-items: center; justify-content: center; }
  .carousel-arrow--prev { left: 64px; }
  .carousel-arrow--next { left: 281px; }
  .card-brand {
    position: absolute; left: 126px; top: 365px; width: 122px; height: 54px;
    background: var(--white); border-radius: 6px; box-shadow: 0 3px 10px rgba(40,55,90,0.14);
    display: flex; align-items: center; justify-content: center;
    font-size: 24px; font-weight: 600; color: #1a3d8f;
  }
  .field-label { position: absolute; font-size: 11px; color: var(--ink-soft); letter-spacing: 0.2px; }
  .field {
    position: absolute; height: 34px; border: 1px solid var(--line); border-radius: 4px;
    font-size: 10.5px; color: #b9bcc2; display: flex; align-items: center; justify-content: space-between; padding: 0 9px; letter-spacing: 0.3px;
  }
  .keypad { position: absolute; left: 0; top: 613px; width: 369px; height: 188px; background: #edf1f8; }
  .key {
    position: absolute; width: 94px; height: 30px; background: var(--white); border-radius: 5px;
    box-shadow: 0 1px 2px rgba(40,55,90,0.06);
    display: flex; align-items: center; justify-content: center; gap: 8px;
    font-size: 15px; color: var(--ink);
  }
  .key small { font-size: 8.5px; letter-spacing: 0.4px; }
</style>
</head>
<body>

<section class="screen screen--donee">
  <div class="donee-photo" role="img" aria-label="Aerial photograph of an ornate tiled mosque with domes and minarets in a dense old city"></div>

  <div class="icon-btn icon-btn--edit">
    <svg width="16" height="16" viewBox="0 0 16 16"><path d="M3 13l1-3.5L11 2.5l2.5 2.5L6.5 12z" fill="#1f3466"/></svg>
  </div>
  <div class="icon-btn icon-btn--menu"></div>

  <svg class="side-tab" width="49" height="78" viewBox="0 0 49 78">
    <defs><linearGradient id="tabFill" x1="0" y1="0" x2="1" y2="1"><stop offset="0" stop-color="#2a4a8f"/><stop offset="1" stop-color="#0f1f4d"/></linearGradient></defs>
    <path d="M14 0H49V78H14L0 39z" fill="url(#tabFill)"/>
    <path d="M27 33l-6 6 6 6M34 33l-6 6 6 6" stroke="#fff" stroke-width="1.8" fill="none"/>
  </svg>

  <div class="donee-card">
    <h1 class="donee-name">Rafiq</h1>
    <div class="pay-badge">Orchard Pay</div>
    <div class="donee-bio">
      <p>I am from Pakistan. I have three kids.</p>
      <p>Lorem ipsum doloret, consectetur lorem adipiscing elit, sed do eiusmod temporn.</p>
    </div>
    <div class="money-tray">
      <div class="coin" role="img" aria-label="Silver one dirham coin"></div>
      <div class="banknote banknote--red" role="img" aria-label="Red five dirham banknote"></div>
      <div class="banknote banknote--green" role="img" aria-label="Green banknote"></div>
    </div>
    <div class="slide-pill">
      <span class="slide-pill__knob"><svg width="9" height="6" viewBox="0 0 9 6"><path d="M1 5l3.5-3.5L8 5" stroke="#fff" stroke-width="1.5" fill="none"/></svg></span>
      SLIDE TO SHUKRAN
    </div>
  </div>
</section>

<section class="screen screen--payment">
  <div class="pay-header"></div>
  <div class="pay-skyline" role="img" aria-label="Faint night skyline of mosque domes and minarets with stars"></div>
  <div class="brand-mark"></div>
  <div class="brand-name">Zakat</div>

  <svg class="pay-sheet" width="369" height="400" viewBox="0 0 369 400">
    <path d="M0 45 Q0 22 30 22 H140 Q160 22 172 10 Q185 -2 198 10 Q210 22 230 22 H339 Q369 22 369 45 V400 H0z" fill="#fff"/>
  </svg>
  <div class="sheet-toggle">
    <svg width="14" height="9" viewBox="0 0 14 9"><path d="M1.5 1.5l5.5 5.5 5.5-5.5" stroke="#fff" stroke-width="2" fill="none"/></svg>
  </div>

  <h2 class="pay-title">Payment Method</h2>
  <div class="carousel-arrow carousel-arrow--prev"><svg width="8" height="10" viewBox="0 0 8 10"><path d="M6 1L2 5l4 4" stroke="#8a8f98" stroke-width="1.3" fill="none"/></svg></div>
  <div class="card-brand">Varda</div>
  <div class="carousel-arrow carousel-arrow--next"><svg width="8" height="10" viewBox="0 0 8 10"><path d="M2 1l4 4-4 4" stroke="#8a8f98" stroke-width="1.3" fill="none"/></svg></div>

  <span class="field-label" style="left:73px;top:451px;">Credit Card Number</span>
  <div class="field" style="left:65px;top:472px;width:240px;">
    1234 1234 1234
    <svg width="22" height="15" viewBox="0 0 22 15"><rect x="1" y="1" width="20" height="13" rx="2" fill="none" stroke="#8a8f98" stroke-width="1.2"/><path d="M1 5h20" stroke="#8a8f98" stroke-width="1.2"/></svg>
  </div>

  <span class="field-label" style="left:73px;top:521px;">Exp Date</span>
  <span class="field-label" style="left:224px;top:521px;">CV</span>
  <div class="field" style="left:65px;top:542px;width:151px;">MM / YY</div>
  <div class="field" style="left:225px;top:542px;width:80px;">
    ***
    <svg width="15" height="15" viewBox="0 0 15 15"><circle cx="7.5" cy="7.5" r="6.5" fill="none" stroke="#8a8f98" stroke-width="1.1"/><path d="M7.5 6.5v4.5M7.5 4v1" stroke="#8a8f98" stroke-width="1.2"/></svg>
  </div>

  <div class="keypad">
    <div class="key" style="left:21px;top:25px;">1 <small>ABC</small></div>
    <div class="key" style="left:137px;top:25px;">2 <small>DEF</small></div>
    <div class="key" style="left:253px;top:25px;">3 <small>GHI</small></div>
    <div class="key" style="left:21px;top:62px;">4 <small>JKL</small></div>
    <div class="key" style="left:137px;top:62px;">5 <small>MNO</small></div>
    <div class="key" style="left:253px;top:62px;">6 <small>PQR</small></div>
    <div class="key" style="left:21px;top:100px;">7 <small>STU</small></div>
    <div class="key" style="left:137px;top:100px;">8 <small>VWX</small></div>
    <div class="key" style="left:253px;top:100px;">9 <small>YZ</small></div>
    <div class="key" style="left:21px;top:142px;"><small>+ * #</small></div>
    <div class="key" style="left:137px;top:142px;">0</div>
    <div class="key" style="left:253px;top:142px;">
      <svg width="16" height="11" viewBox="0 0 16 11"><path d="M5 1h10v9H5L1 5.5z" fill="none" stroke="#555" stroke-width="1.1"/><path d="M8 3.5l4 4M12 3.5l-4 4" stroke="#555" stroke-width="1.1"/></svg>
    </div>
  </div>
</section>

</body>
</html>
```